Clean Landing Page - Design and Code

Need to create a similar landing page to example i have supplied. Need versions for Desktop, tablet and mobile. Letting the design chose color scheme based on description.

We want it to seem fresh, clean and cool.

We are basing it off this example http://torvanmesk.com/

Target Market(s)

young ambitious entreprerial women

Coding

Coded - Design and coding required

Number of Pages Required

3 page

Font styles to use
Sans Serif

Requirements
Must have
• Must be designed for responsive functionality.

```html
<!DOCTYPE html>
<html lang="en">
<head>
<meta charset="utf-8">
<title>Mara Vellin – Glow Social Club</title>
<link href="https://fonts.googleapis.com/css2?family=Open+Sans:wght@400;600;700;800&family=Lato:wght@400;700;900&family=Exo+2:wght@400;500&display=swap" rel="stylesheet">
<style>
  :root {
    --hero-bg: #e7e5e1;
    --hero-bg-light: #efeeeb;
    --brand-blue: #1f5a96;
    --ink-grey: #454545;
    --rule-blue: #6f86d6;
    --cta-blue: #5572dd;
    --white: #ffffff;
    --section-ink: #1c1c1c;
    --card-border: #e1e1e1;
    --icon-blue: #29abe2;
  }
  * { margin: 0; padding: 0; box-sizing: border-box; }
  html, body {
    width: 1200px; height: 962px; overflow: hidden; background: var(--white);
  }
  .page { position: relative; width: 1200px; height: 962px; overflow: hidden; }

  .hero {
    position: absolute; left: 0; top: 0; width: 1200px; height: 596px;
    background: linear-gradient(180deg, var(--hero-bg-light), var(--hero-bg));
  }
  .hero-portrait {
    position: absolute; left: 210px; top: 54px; width: 336px; height: 542px;
    border-radius: 150px 150px 0 0;
    background: linear-gradient(180deg, #3a2a24 0%, #c9a592 30%, #f3efea 55%, #e9e4de 85%, #2b2522 100%);
  }
  .hero-copy { position: absolute; left: 601px; top: 0; width: 520px; }
  .hero-name {
    position: absolute; left: 0; top: 57px; white-space: nowrap;
    font-family: "Open Sans", sans-serif; font-weight: 400; font-size: 44px;
    color: var(--brand-blue); line-height: 56px; letter-spacing: -1px;
  }
  .hero-title {
    position: absolute; left: 0; top: 108px; white-space: nowrap;
    font-family: "Open Sans", sans-serif; font-weight: 700; font-size: 42px;
    color: var(--ink-grey); line-height: 56px; letter-spacing: -1px;
  }
  .hero-rule {
    position: absolute; left: 0; top: 184px;
    width: 478px; height: 2px; background: var(--rule-blue);
  }
  .hero-headline {
    position: absolute; left: 0; top: 217px; white-space: nowrap;
    font-family: "Lato", sans-serif; font-weight: 400; font-size: 52px;
    color: var(--ink-grey); line-height: 63px; letter-spacing: -0.3px;
  }
  .hero-headline strong { font-weight: 900; }
  .cta-button {
    position: absolute; left: 0; top: 455px;
    display: block; width: 496px; height: 82px; border-radius: 41px;
    background: var(--cta-blue); color: var(--white); text-align: center;
    font-family: "Open Sans", sans-serif; font-weight: 800; font-size: 22px;
    line-height: 82px; text-decoration: none; letter-spacing: 0.2px; white-space: nowrap;
  }

  .benefits { position: absolute; left: 0; top: 596px; width: 1200px; height: 366px; }
  .benefits-heading {
    position: absolute; left: 0; top: 32px; width: 1200px; text-align: center;
    font-family: "Exo 2", sans-serif; font-weight: 400; font-size: 32px; line-height: 40px;
    color: var(--section-ink); letter-spacing: 0.5px;
  }
  .benefit-list { position: absolute; left: 117px; top: 110px; display: flex; gap: 20px; }
  .benefit-card {
    position: relative; width: 230px; height: 260px;
    border: 2px solid var(--card-border); border-bottom: none; text-align: center;
  }
  .benefit-icon { position: absolute; left: 63px; top: 33px; }
  .benefit-title {
    position: absolute; left: 0; top: 154px; width: 226px; height: 81px;
    display: flex; align-items: center; justify-content: center; padding: 0 12px;
    font-family: "Exo 2", sans-serif; font-weight: 400; font-size: 19px; line-height: 21px;
    color: var(--section-ink); text-transform: uppercase;
  }
</style>
</head>
<body>
<div class="page">
  <header class="hero">
    <div class="hero-portrait" role="img" aria-label="Portrait photo of a smiling woman with long dark hair in a white lace top"></div>
    <div class="hero-copy">
      <h1 class="hero-name">MARA VELLIN</h1>
      <p class="hero-title">GLOW SOCIAL CLUB</p>
      <div class="hero-rule"></div>
      <h2 class="hero-headline">The <strong>Advanced</strong> Guide<br>to Becoming a <strong>Paid</strong><br>Social Media Influencer</h2>
      <a class="cta-button" href="#">YES, I WANT MARA TO SHOW ME HOW</a>
    </div>
  </header>

  <section class="benefits">
    <h3 class="benefits-heading">HERE IS WHAT I'M GOING TO SHOW YOU</h3>
    <div class="benefit-list">
      <article class="benefit-card">
        <svg class="benefit-icon" width="100" height="100" viewBox="0 0 100 100">
          <circle cx="50" cy="50" r="50" fill="var(--icon-blue)"/>
          <circle cx="50" cy="52" r="20" fill="none" stroke="#fff" stroke-width="6"/>
          <circle cx="50" cy="52" r="7" fill="#fff"/>
          <path d="M42 28 L58 28 L60 34 L40 34 Z" fill="#fff"/>
        </svg>
        <p class="benefit-title">The little-known secrets to grow a following</p>
      </article>
      <article class="benefit-card">
        <svg class="benefit-icon" width="100" height="100" viewBox="0 0 100 100">
          <circle cx="50" cy="50" r="50" fill="var(--icon-blue)"/>
          <path d="M56 22 L36 54 L49 54 L42 78 L66 44 L53 44 Z" fill="#fff"/>
        </svg>
        <p class="benefit-title">How to properly price your posts</p>
      </article>
      <article class="benefit-card">
        <svg class="benefit-icon" width="100" height="100" viewBox="0 0 100 100">
          <circle cx="50" cy="50" r="50" fill="var(--icon-blue)"/>
          <path d="M36 72 L36 42 Q36 37 40 37 Q44 37 44 42 L44 30 Q44 25 48 25 Q52 25 52 30 L52 40 L52 32 Q52 28 56 28 Q60 28 60 32 L60 52 L66 46 Q70 43 73 46 L60 70 Q56 76 50 76 L42 76 Q36 76 36 72 Z" fill="#fff"/>
        </svg>
        <p class="benefit-title">How to negotiate with brands</p>
      </article>
      <article class="benefit-card">
        <svg class="benefit-icon" width="100" height="100" viewBox="0 0 100 100">
          <circle cx="50" cy="50" r="50" fill="var(--icon-blue)"/>
          <path d="M50 24 Q68 24 68 42 Q68 52 60 58 L60 64 L40 64 L40 58 Q32 52 32 42 Q32 24 50 24 Z" fill="#fff"/>
          <rect x="41" y="67" width="18" height="4" rx="2" fill="#fff"/>
          <rect x="43" y="73" width="14" height="4" rx="2" fill="#fff"/>
        </svg>
        <p class="benefit-title">How to attract brands to your profile</p>
      </article>
    </div>
  </section>
</div>
</body>
</html>
```